Tradeshwo display 8x10 high resolution backdrop

I created a backdrop I wanted to use via Chat GPT but the image isn't high quality enough for print so I want someone to recreate it as close as possible to my creation. See attached, TY!

```html
<!DOCTYPE html>
<html lang="en">
<head>
<meta charset="utf-8">
<title>HydraCore Systems – Trade Show Backdrop</title>
<link href="https://fonts.googleapis.com/css2?family=Kanit:wght@600;700&family=Roboto+Condensed:wght@400;500;700&display=swap" rel="stylesheet">
<style>
:root{
  --navy:#0a1a36;
  --navy-2:#0f2550;
  --royal:#1d43b8;
  --royal-2:#2f5fd6;
  --sky:#3b9ae6;
  --ink:#141414;
  --text:#222;
  --rule:#c9d2e3;
  --white:#ffffff;
}
*{box-sizing:border-box;margin:0;padding:0}
html,body{width:1200px;height:1000px;overflow:hidden;background:#fff}
.backdrop{position:relative;width:1200px;height:1000px;overflow:hidden;background:var(--white);font-family:"Roboto Condensed",Arial,sans-serif;color:var(--text)}
.backdrop-shapes{position:absolute;inset:0}

/* brand */
.brand{position:absolute;left:54px;top:200px;display:flex;align-items:center;gap:12px}
.brand-dot{width:26px;height:26px;border-radius:50%;background:var(--royal)}
.brand-name{font-family:"Kanit",Arial,sans-serif;font-weight:700;font-size:34px;color:var(--royal);letter-spacing:.5px}

/* value icons */
.values{position:absolute;left:448px;top:158px;display:flex}
.value{width:88px;height:110px;border-left:1.5px solid var(--rule);display:flex;flex-direction:column;align-items:center;gap:8px;padding-top:4px}
.value:first-child{border-left:1.5px solid var(--rule)}
.value svg{width:44px;height:44px}
.value span{font-size:12.5px;font-weight:500;line-height:1.25;text-align:center;color:var(--ink);letter-spacing:.4px}

/* headline */
.headline{position:absolute;left:54px;top:320px;font-family:"Kanit",Arial,sans-serif;font-weight:700;text-transform:uppercase;line-height:1}
.headline-top{display:block;font-size:58px;color:var(--ink);letter-spacing:1px}
.headline-main{display:block;font-size:70px;margin-top:6px;letter-spacing:1px;background:linear-gradient(180deg,#3668e0 0%,#1a3aa8 100%);-webkit-background-clip:text;background-clip:text;color:transparent}
.tagline{position:absolute;left:54px;top:492px;width:770px;display:flex;align-items:center;gap:16px;font-size:18px;font-weight:700;letter-spacing:4px;color:var(--ink)}
.tagline::before,.tagline::after{content:"";flex:1;height:2px;background:var(--navy-2)}

/* banner */
.banner{position:absolute;left:56px;top:520px;width:790px;height:46px;background:linear-gradient(90deg,#1a3a9e,#2a56cc);clip-path:polygon(0 0,97% 0,100% 50%,97% 100%,0 100%);display:flex;align-items:center;padding-left:60px;color:#fff;font-weight:700;font-size:17px;letter-spacing:3px}

/* products */
.products{position:absolute;left:24px;top:580px;display:flex}
.product{width:134px;padding:0 6px;text-align:center;border-left:1px solid var(--rule)}
.product:first-child{border-left:none}
.product-visual{height:120px;margin:0 auto 12px;width:110px;border-radius:10px}
.visual-pump{background:radial-gradient(circle at 45% 50%,#2f5fd6,#17357f 75%)}
.visual-motor{background:radial-gradient(circle at 50% 45%,#2d5bc9,#0f2a6b 75%)}
.visual-blower{background:radial-gradient(circle at 50% 45%,#b9bcc1,#6d7279 75%)}
.visual-drive{width:70px;background:linear-gradient(180deg,#2a3a55,#0e1a2e)}
.visual-valve{background:radial-gradient(circle at 50% 55%,#2a4fb5,#8b9098 80%)}
.visual-turnkey{display:flex;align-items:center;justify-content:center;background:none}
.visual-turnkey svg{width:86px;height:86px}
.product h3{font-size:14px;font-weight:700;color:var(--royal);text-transform:uppercase;margin-bottom:8px}
.product p{font-size:11.5px;line-height:1.6;color:var(--ink)}

/* features */
.features{position:absolute;left:955px;top:408px;display:flex;flex-direction:column;gap:12px}
.feature{width:260px;height:86px;background:linear-gradient(90deg,rgba(23,56,140,.9),rgba(10,26,60,.9));clip-path:polygon(7% 0,100% 0,100% 100%,7% 100%,0 50%);display:flex;align-items:center;gap:14px;padding-left:24px;border:1px solid rgba(120,170,240,.4)}
.feature-icon{width:56px;height:56px;border-radius:50%;border:2px solid #fff;display:flex;align-items:center;justify-content:center;flex:none}
.feature-icon svg{width:30px;height:30px}
.feature span{color:#fff;font-size:15px;font-weight:500;letter-spacing:1px;line-height:1.25;text-transform:uppercase}

/* footer */
.footer{position:absolute;left:0;right:0;top:900px;height:100px;display:flex;align-items:center;color:#fff}
.service{display:flex;align-items:center;gap:12px;padding-left:58px;width:540px}
.service-pin{width:40px;height:40px;border-radius:50%;background:var(--sky);display:flex;align-items:center;justify-content:center}
.service-pin svg{width:20px;height:20px}
.service-label{font-size:15px;letter-spacing:.5px}
.service-states{font-size:13px;font-weight:500;letter-spacing:.5px;margin-top:2px}
.divider{width:1.5px;height:46px;background:rgba(255,255,255,.6)}
.site{width:330px;text-align:center;font-size:22px;font-weight:700}
.site b{color:var(--sky)}
.partner{padding-left:30px;font-size:14px;letter-spacing:.5px;line-height:1.2}
.partner strong{display:block;font-size:20px;color:var(--sky);font-weight:700}
</style>
</head>
<body>
<div class="backdrop">

  <svg class="backdrop-shapes" viewBox="0 0 1200 1000" aria-hidden="false">
    <defs>
      <linearGradient id="plantPhoto" x1="0" y1="0" x2="0" y2="1">
        <stop offset="0" stop-color="#2a6fbf"/>
        <stop offset=".45" stop-color="#9cc3e8"/>
        <stop offset=".6" stop-color="#e9c98f"/>
        <stop offset=".75" stop-color="#3f6f9e"/>
        <stop offset="1" stop-color="#1d4f88"/>
      </linearGradient>
      <linearGradient id="panelNavy" x1="0" y1="0" x2="1" y2="1">
        <stop offset="0" stop-color="#0f2a64"/>
        <stop offset="1" stop-color="#081630"/>
      </linearGradient>
      <linearGradient id="waterGlow" x1="0" y1="0" x2="1" y2="0">
        <stop offset="0" stop-color="#0a1a36"/>
        <stop offset=".6" stop-color="#1b4fa6"/>
        <stop offset="1" stop-color="#3b9ae6"/>
      </linearGradient>
    </defs>
    <!-- right navy panel -->
    <path d="M690 0 C780 170 840 360 880 520 L900 900 L1200 900 V0 Z" fill="url(#panelNavy)"/>
    <!-- swoosh lines -->
    <path d="M700 0 C790 170 850 350 900 500" fill="none" stroke="#3b9ae6" stroke-width="8"/>
    <path d="M718 0 C808 165 868 340 920 480" fill="none" stroke="#a9cdf2" stroke-width="4"/>
    <!-- treatment plant photo -->
    <path d="M740 0 H1200 V420 H920 C860 300 810 150 740 0 Z" fill="url(#plantPhoto)" role="img" aria-label="Photo of a water treatment plant with clarifier tanks at sunrise"/>
    <!-- footer band -->
    <path d="M0 870 C320 820 760 860 1200 820 V1000 H0 Z" fill="var(--navy)"/>
    <path d="M640 880 C820 850 1000 830 1200 790 V900 C1000 900 820 900 640 880 Z" fill="url(#waterGlow)" opacity=".85" role="img" aria-label="Blue water wave texture"/>
  </svg>

  <div class="brand">
    <span class="brand-dot"></span>
    <span class="brand-name">HydraCore Systems</span>
  </div>

  <div class="values">
    <div class="value">
      <svg viewBox="0 0 44 44" fill="none" stroke="#1d43b8" stroke-width="2"><circle cx="22" cy="17" r="12"/><path d="M16 17l4 4 8-8"/><path d="M14 27l-4 12 6-3 3 5 3-10M30 27l4 12-6-3-3 5-3-10"/></svg>
      <span>QUALITY<br>BRANDS</span>
    </div>
    <div class="value">
      <svg viewBox="0 0 44 44" fill="none" stroke="#1d43b8" stroke-width="2"><circle cx="22" cy="22" r="6"/><path d="M22 4v6M22 34v6M4 22h6M34 22h6M9 9l4 4M31 31l4 4M9 35l4-4M31 13l4-4"/><circle cx="22" cy="22" r="12"/></svg>
      <span>ENGINEERED<br>SOLUTIONS</span>
    </div>
    <div class="value">
      <svg viewBox="0 0 44 44" fill="none" stroke="#1d43b8" stroke-width="2"><path d="M8 24v-4a14 14 0 0 1 28 0v4"/><rect x="6" y="22" width="7" height="11" rx="2"/><rect x="31" y="22" width="7" height="11" rx="2"/><path d="M34 33c0 5-6 6-10 6"/></svg>
      <span>EXPERT<br>SUPPORT</span>
    </div>
    <div class="value">
      <svg viewBox="0 0 44 44" fill="none" stroke="#1d43b8" stroke-width="2"><path d="M2 16l8-4 8 4 6-3 8 3 10-4v14l-8 4-8 8-4-3-4 3-4-4-4 2-4-6-4-2z"/><path d="M18 16l-4 6 4 2 6-6"/></svg>
      <span>TURNKEY<br>DELIVERY</span>
    </div>
  </div>

  <h1 class="headline">
    <span class="headline-top">Solutions That</span>
    <span class="headline-main">Keep Water Moving</span>
  </h1>

  <div class="tagline" style="top:470px">EXPERTISE. RELIABILITY. RESULTS.</div>

  <div class="banner">COMPLETE SOLUTIONS FOR THE WATER &amp; WASTEWATER INDUSTRY</div>

  <div class="products">
    <div class="product">
      <div class="product-visual visual-pump" role="img" aria-label="Split-case centrifugal pump"></div>
      <h3>Pumps</h3>
      <p>Industry leading pumps built for performance, efficiency &amp; reliability.</p>
    </div>
    <div class="product">
      <div class="product-visual visual-motor" role="img" aria-label="Electric motor"></div>
      <h3>Motors</h3>
      <p>High efficiency motors engineered for durability and long life.</p>
    </div>
    <div class="product">
      <div class="product-visual visual-blower" role="img" aria-label="Positive displacement blower"></div>
      <h3>Blowers</h3>
      <p>Aerion PD positive displacement blowers for reliable, energy efficient performance.</p>
    </div>
    <div class="product">
      <div class="product-visual visual-drive" role="img" aria-label="Variable frequency drive unit"></div>
      <h3>VFD &amp; Controls</h3>
      <p>Precision control and energy savings through advanced VFD solutions.</p>
    </div>
    <div class="product">
      <div class="product-visual visual-valve" role="img" aria-label="Actuated control valve"></div>
      <h3>Automation &amp; Valves</h3>
      <p>Smart automation and reliable valves for optimized system performance.</p>
    </div>
    <div class="product">
      <div class="product-visual visual-turnkey">
        <svg viewBox="0 0 86 86" fill="#1d43b8"><path d="M43 6l5 0 2 7 6 3 6-4 4 4-4 6 3 6 7 2v6l-7 2-3 6 4 6-4 4-6-4-6 3-2 7h-6l-2-7-6-3-6 4-4-4 4-6-3-6-7-2v-6l7-2 3-6-4-6 4-4 6 4 6-3 2-7z"/><circle cx="45" cy="33" r="11" fill="#fff"/><path d="M45 25c3 4 5 7 5 9a5 5 0 0 1-10 0c0-2 2-5 5-9z"/><path d="M6 66c8-6 16-8 24-6l14 2c4 1 4 6 0 6H32l14 1 18-8c4-2 7 3 3 5L46 78H20l-8 4z"/></svg>
      </div>
      <h3>Turnkey Solutions</h3>
      <p>Complete systems designed, integrated and supported by HydraCore.</p>
    </div>
  </div>

  <div class="features">
    <div class="feature">
      <div class="feature-icon"><svg viewBox="0 0 30 30" fill="none" stroke="#fff" stroke-width="2"><path d="M15 3c5 7 8 11 8 15a8 8 0 0 1-16 0c0-4 3-8 8-15z"/></svg></div>
      <span>Water &amp;<br>Wastewater<br>Expertise</span>
    </div>
    <div class="feature">
      <div class="feature-icon"><svg viewBox="0 0 30 30" fill="none" stroke="#fff" stroke-width="2"><path d="M15 3l10 4v7c0 7-5 11-10 13C10 25 5 21 5 14V7z"/><path d="M10 15l4 4 6-7"/></svg></div>
      <span>Trusted<br>Products</span>
    </div>
    <div class="feature">
      <div class="feature-icon"><svg viewBox="0 0 30 30" fill="none" stroke="#fff" stroke-width="2"><path d="M5 17v-3a10 10 0 0 1 20 0v3"/><rect x="4" y="15" width="5" height="8" rx="1"/><rect x="21" y="15" width="5" height="8" rx="1"/><path d="M23 23c0 3-4 4-7 4"/></svg></div>
      <span>Local Support<br>You Can Count On</span>
    </div>
    <div class="feature">
      <div class="feature-icon"><svg viewBox="0 0 30 30" fill="#fff"><rect x="5" y="18" width="4" height="8"/><rect x="11" y="14" width="4" height="12"/><rect x="17" y="10" width="4" height="16"/><path d="M5 12l7-5 5 3 8-6" fill="none" stroke="#fff" stroke-width="2"/></svg></div>
      <span>Built for Performance.<br>Focused on<br>Your Success.</span>
    </div>
  </div>

  <div class="footer">
    <div class="service">
      <div class="service-pin"><svg viewBox="0 0 20 20" fill="#fff"><path d="M10 1a6 6 0 0 1 6 6c0 5-6 12-6 12S4 12 4 7a6 6 0 0 1 6-6z"/><circle cx="10" cy="7" r="2.3" fill="#3b9ae6"/></svg></div>
      <div>
        <div class="service-label">SERVICING</div>
        <div class="service-states">VIRGINIA &nbsp;|&nbsp; NORTH CAROLINA &nbsp;|&nbsp; MARYLAND &nbsp;|&nbsp; DELAWARE</div>
      </div>
    </div>
    <div class="divider"></div>
    <div class="site">www.<b>hydracore-flow</b>.com</div>
    <div class="divider"></div>
    <div class="partner">YOUR PARTNER FOR<strong>A BETTER FLOW FORWARD</strong></div>
  </div>

</div>
</body>
</html>
```